Business Cards for a Junk Removal Company

Hello,
We are looking to have business cards designed that are simple, bold, easy to read, and right to the point. Please see the attachments for our logo files. We want the card to be yellow on both sides ( Color code Yellow: #FFE01B). The logo text font is (Rockstar Extra Bold) and this is also in the files attached. Please make the text black for the logo. On the back side of the card, you can use white and black for text. Thank you in advance for your hard work!

Front of card-
Harbor Haul Away (logo)
Back of card-
Harbor Haul Away
Donate - Recycle - Dispose
555-271-8093
www.harborhaulaway.example
info@harborhaulaway.example

Industry/Entity Type

Junk removal

Contact Information for Business Card

FRONT OF CARD- Harbor Haul Away (logo) BACK OF CARD- Harbor Haul Away Donate - Recycle - Dispose 555-271-8093 www.harborhaulaway.example info@harborhaulaway.example

Font styles to use
Other font styles liked:
• Rockstar Extra Bold

Colors
FFF300
FFF600
FEFA6F
FFFEC7
FFFEE8

Requirements
Must have
• Must have color code Yellow: #FFE01B for the background of front and back of the card

```html
<!DOCTYPE html>
<html lang="en">
<head>
<meta charset="utf-8">
<title>Harbor Haul Away – Business Cards</title>
<link rel="stylesheet" href="https://fonts.googleapis.com/css2?family=Archivo+Black&family=Roboto:wght@500;700&display=swap">
<style>
  :root {
    --card-yellow: #FFE01B;
    --ink: #0b0b0b;
    --paper-white: #ffffff;
    --stage: #3a3a3c;
  }
  * { box-sizing: border-box; margin: 0; padding: 0; }
  html, body {
    width: 1200px;
    height: 900px;
    overflow: hidden;
    background: var(--stage);
  }
  .stage {
    position: relative;
    width: 1200px;
    height: 900px;
  }
  .card {
    position: absolute;
    left: 250px;
    width: 700px;
    height: 400px;
    background: var(--card-yellow);
    overflow: hidden;
  }
  .card--back { top: 40px; }
  .card--front { top: 460px; }

  .brand-name {
    font-family: "Archivo Black", sans-serif;
    color: var(--ink);
    text-transform: uppercase;
    line-height: 0.95;
    white-space: nowrap;
  }

  /* Back side */
  .card--back .brand-name {
    position: absolute;
    left: 44px;
    top: 104px;
    width: 280px;
    font-size: 40px;
  }
  .divider-vertical {
    position: absolute;
    left: 345px;
    top: 50px;
    width: 1.5px;
    height: 190px;
    background: var(--ink);
  }
  .contact-list {
    position: absolute;
    left: 372px;
    top: 72px;
    list-style: none;
    font-family: "Roboto", sans-serif;
    font-weight: 700;
    color: var(--ink);
  }
  .contact-list li {
    display: flex;
    align-items: center;
    gap: 9px;
    font-size: 17px;
    line-height: 1;
    margin-bottom: 14px;
    white-space: nowrap;
  }
  .contact-list .phone { font-size: 20px; }
  .contact-icon { width: 16px; height: 16px; flex: none; }
  .tagline-band {
    position: absolute;
    left: 0;
    top: 262px;
    width: 100%;
    height: 74px;
    background: var(--ink);
    display: flex;
    align-items: center;
    justify-content: center;
  }
  .tagline {
    font-family: "Archivo Black", sans-serif;
    color: var(--card-yellow);
    font-size: 20px;
    letter-spacing: 0.28em;
    text-transform: uppercase;
  }

  /* Front side */
  .card--front .brand-name {
    position: absolute;
    left: 0;
    width: 100%;
    top: 92px;
    text-align: center;
    font-size: 74px;
  }
  .divider-horizontal {
    position: absolute;
    left: 140px;
    top: 262px;
    width: 420px;
    height: 2px;
    background: var(--ink);
  }
  .web-address {
    position: absolute;
    left: 0;
    width: 100%;
    top: 282px;
    text-align: center;
    font-family: "Archivo Black", sans-serif;
    color: var(--paper-white);
    font-size: 19px;
    letter-spacing: 0.2em;
  }
</style>
</head>
<body>
<main class="stage">

  <section class="card card--back" aria-label="Back of business card">
    <h2 class="brand-name">Harbor<br>Haul Away</h2>
    <span class="divider-vertical"></span>
    <ul class="contact-list">
      <li class="phone">
        <svg class="contact-icon" viewBox="0 0 16 16" aria-hidden="true"><path d="M3 1.5h3l1.2 3.2-1.8 1.2a8.5 8.5 0 0 0 4.7 4.7l1.2-1.8 3.2 1.2v3c0 .6-.5 1.1-1.1 1.1A12.6 12.6 0 0 1 1.9 2.6c0-.6.5-1.1 1.1-1.1z" fill="#0b0b0b"/></svg>
        555-271-8093
      </li>
      <li>
        <svg class="contact-icon" viewBox="0 0 16 16" aria-hidden="true"><rect x="1" y="3" width="14" height="10" rx="1" fill="#0b0b0b"/><path d="M1.5 3.8 8 9l6.5-5.2" stroke="#FFE01B" stroke-width="1.3" fill="none"/></svg>
        info@harborhaulaway.example
      </li>
      <li>
        <svg class="contact-icon" viewBox="0 0 16 16" aria-hidden="true"><circle cx="8" cy="8" r="6.5" fill="none" stroke="#0b0b0b" stroke-width="1.5"/><ellipse cx="8" cy="8" rx="2.8" ry="6.5" fill="none" stroke="#0b0b0b" stroke-width="1.2"/><path d="M1.5 8h13" stroke="#0b0b0b" stroke-width="1.2"/></svg>
        www.harborhaulaway.example
      </li>
    </ul>
    <div class="tagline-band">
      <p class="tagline">Donate - Recycle - Dispose</p>
    </div>
  </section>

  <section class="card card--front" aria-label="Front of business card">
    <h1 class="brand-name">Harbor<br>Haul Away</h1>
    <span class="divider-horizontal"></span>
    <p class="web-address">WWW.HARBORHAULAWAY.EXAMPLE</p>
  </section>

</main>
</body>
</html>
```